Allied Health team of Physiotherapists & Occupational Therapists seek a business card design

We have our new logo, we now need our new business cards and stationary. Willowmere: Oedema & Family Clinic is seeking a generic card design to represent our whole team and individual cards for each therapist that incorporates our new logo to communicate our holistic approach that is calming, nuturing, supportive and welcoming.
Our Physiotherapists and Occupational Therapists assess, treat and provide education for people who are at risk of or who have lymphoedema. This is often as a result of treatment for cancer. We provide pre-operative and post-operative management and cancer rehabilitation in our Pilates studio. Our team also consists of Physiotherapists who have a strong interest in pelvic floor and continence management for both men and women.

Target Market(s)

Mainly women health conscious

Industry/Entity Type

Allied Health: Physiotherapy / Occupational Therapy

Contact Information for Business Card

Address: 14 Tannerly Ave Kellbrook 3905 Phone: 84317756 fax: 8431 7759 Email: info@willowmerecareco.com.au Website: willowmerecareco.com.au Facebook address: facebook.com/WillowmereOedemaAndFamilyCareCentre. Room to write appointments. Individual cards need to have name, office email and individual email and professional details

Requirements
Must have
• Logo as per uploaded documents

```html
<!DOCTYPE html>
<html lang="en">
<head>
<meta charset="utf-8">
<title>Willowmere: Oedema &amp; Family Clinic — Business Cards</title>
<link rel="stylesheet" href="https://fonts.googleapis.com/css2?family=Noto+Serif:ital,wght@0,400;0,700;1,700&family=Abel&display=swap">
<style>
  :root {
    --peach: #f0a877;
    --slate: #505355;
    --paper: #f7f7f7;
    --ink: #3c3c3c;
    --ink-dark: #141414;
    --cream: #fdebd3;
    --mist: #d8d8d8;
    --backdrop: #e8e5e1;
    --serif: "Noto Serif", Georgia, serif;
    --condensed: "Abel", "Arial Narrow", sans-serif;
  }
  * { box-sizing: border-box; margin: 0; padding: 0; }
  html, body { width: 1200px; height: 900px; overflow: hidden; }
  body { background: var(--backdrop); position: relative; }

  .card {
    position: absolute;
    left: 270px;
    width: 660px;
    height: 377px;
    background: var(--paper);
    overflow: hidden;
    box-shadow: 0 6px 18px rgba(0,0,0,.16);
  }
  .card--contact { top: 44px; }
  .card--team { top: 479px; }

  /* brand block */
  .brand-panel {
    position: absolute;
    background: var(--peach);
    display: flex;
    align-items: center;
    justify-content: center;
  }
  .brand-ring {
    width: 78%;
    aspect-ratio: 1;
    border: 2px solid var(--cream);
    border-radius: 50%;
    display: flex;
    align-items: center;
    justify-content: center;
  }
  .brand-name {
    font-family: var(--serif);
    font-weight: 400;
    color: var(--cream);
    text-align: center;
    line-height: 1.2;
  }

  /* contact side */
  .card--contact .brand-panel { left: 40px; top: 50px; width: 250px; height: 225px; }
  .card--contact .brand-name { font-size: 24px; }
  .contact-band { position: absolute; left: 0; top: 308px; width: 302px; height: 69px; background: var(--peach); }
  .contact-strip { position: absolute; left: 302px; top: 300px; right: 0; height: 30px; background: var(--slate); }
  .contact-rule { position: absolute; left: 300px; top: 0; width: 2px; height: 300px; background: var(--peach); }
  .brand-faint {
    position: absolute; right: 34px; top: 26px;
    font-family: var(--serif); font-size: 18px; color: var(--mist);
  }
  .contact-list { position: absolute; left: 288px; top: 104px; list-style: none; }
  .contact-item { display: flex; align-items: center; height: 48px; }
  .contact-icon {
    width: 26px; height: 26px; border-radius: 50%;
    background: var(--peach); flex: none;
    display: flex; align-items: center; justify-content: center;
  }
  .contact-text {
    margin-left: 16px;
    font-family: var(--serif); font-weight: 700;
    font-size: 15px; color: var(--ink); line-height: 1.25;
  }

  /* team side */
  .card--team .brand-panel { left: 455px; top: 112px; width: 175px; height: 165px; }
  .card--team .brand-name { font-size: 18px; }
  .team-list { position: absolute; left: 60px; top: 30px; }
  .member { margin-bottom: 16px; }
  .member-name {
    font-family: var(--serif); font-weight: 700; font-style: italic;
    font-size: 19px; color: var(--ink-dark); line-height: 1.2;
  }
  .member-role {
    font-family: var(--condensed);
    font-size: 17px; color: var(--ink-dark); line-height: 1.18;
  }
  .team-band { position: absolute; left: 0; top: 305px; right: 0; bottom: 0; background: var(--slate); }
  .site-pill {
    position: absolute; left: 168px; top: 285px; width: 276px; height: 42px;
    background: var(--peach); border-radius: 8px;
    display: flex; align-items: center; justify-content: center;
    font-family: var(--serif); font-weight: 700;
    font-size: 17px; color: var(--slate);
  }
</style>
</head>
<body>

<section class="card card--contact" aria-label="Clinic contact side">
  <div class="brand-panel">
    <div class="brand-ring"><span class="brand-name">Willowmere</span></div>
  </div>
  <div class="contact-band"></div>
  <div class="contact-strip"></div>
  <div class="contact-rule"></div>
  <span class="brand-faint">Willowmere</span>

  <ul class="contact-list">
    <li class="contact-item">
      <span class="contact-icon">
        <svg width="14" height="14" viewBox="0 0 24 24" fill="none" stroke="#fff" stroke-width="2.2"><path d="M12 22s7-7 7-12a7 7 0 0 0-14 0c0 5 7 12 7 12z"/><circle cx="12" cy="10" r="2.5"/></svg>
      </span>
      <span class="contact-text">14 Tannerly Ave,<br>Kellbrook 3905</span>
    </li>
    <li class="contact-item">
      <span class="contact-icon">
        <svg width="14" height="14" viewBox="0 0 24 24" fill="none" stroke="#fff" stroke-width="2.2"><path d="M5 3h4l2 5-2.5 1.5a11 11 0 0 0 6 6L16 13l5 2v4a2 2 0 0 1-2 2A17 17 0 0 1 3 5a2 2 0 0 1 2-2z"/></svg>
      </span>
      <span class="contact-text">8431 7756&nbsp;&nbsp;Fax: 8431 7759</span>
    </li>
    <li class="contact-item">
      <span class="contact-icon">
        <svg width="14" height="14" viewBox="0 0 24 24" fill="none" stroke="#fff" stroke-width="2.2"><rect x="3" y="5" width="18" height="14" rx="2"/><path d="M3 7l9 6 9-6"/></svg>
      </span>
      <span class="contact-text">info@willowmerecareco.com.au</span>
    </li>
    <li class="contact-item">
      <span class="contact-icon">
        <svg width="14" height="14" viewBox="0 0 24 24" fill="none" stroke="#fff" stroke-width="2.2"><circle cx="12" cy="12" r="9"/><path d="M3 12h18M12 3a14 14 0 0 1 0 18M12 3a14 14 0 0 0 0 18"/></svg>
      </span>
      <span class="contact-text">willowmerecareco.com.au</span>
    </li>
  </ul>
</section>

<section class="card card--team" aria-label="Team side">
  <div class="team-list">
    <div class="member">
      <p class="member-name">Mirella Ashcombe</p>
      <p class="member-role">Physiotherapist</p>
      <p class="member-role">Lymphoedema &amp; Oncology Rehabilitation</p>
      <p class="member-role">Continence &amp; Pelvic Floor</p>
    </div>
    <div class="member">
      <p class="member-name">Tamsin Holloway</p>
      <p class="member-role">Physiotherapist</p>
      <p class="member-role">Pelvic Health</p>
    </div>
    <div class="member">
      <p class="member-name">Corinne Vale</p>
      <p class="member-role">Occupational Therapist</p>
      <p class="member-role">Lymphoedema Therapist</p>
    </div>
  </div>

  <div class="brand-panel">
    <div class="brand-ring"><span class="brand-name">Willowmere</span></div>
  </div>

  <div class="team-band"></div>
  <div class="site-pill">willowmerecareco.com.au</div>
</section>

</body>
</html>
```